Business Card Design for a Personal Trainer

I need a business card design for my job as a personal trainer. It should have a unique, modern and exclusive design. On the front there should be only my logo with my name and my job. 0163/2918374 Tobias Kellinger Lindenfeldweg 14 80412 Munich Germany The most important contact information is the web adress. it can be bigger than the rest, but its not necessary. The card should be 8,5cmx5,5cm big. Font: Roboto. Colors: black, white, gray, 56c1ff.

```html
<!DOCTYPE html>
<html lang="de">
<head>
<meta charset="utf-8">
<title>Tobias Kellinger – Visitenkarte</title>
<link href="https://fonts.googleapis.com/css2?family=Roboto:wght@300;400;500;700&display=swap" rel="stylesheet">
<style>
  :root {
    --page-bg: #e9e8e8;
    --brand-blue: #62b9e8;
    --brand-blue-light: #74c3ee;
    --white: #ffffff;
    --text-dark: #3f3f3f;
    --photo-dark: #4a4a4a;
    --photo-light: #d9d9d9;
  }
  html, body {
    margin: 0;
    padding: 0;
    width: 1200px;
    height: 1000px;
    overflow: hidden;
    background: var(--page-bg);
    font-family: "Roboto", sans-serif;
  }
  .canvas { position: relative; width: 1200px; height: 1000px; }
  .card {
    position: absolute;
    left: 230px;
    width: 738px;
    overflow: hidden;
  }
  .card-front {
    top: 55px;
    height: 415px;
    background: linear-gradient(135deg, var(--brand-blue-light) 0%, var(--brand-blue) 100%);
    color: var(--white);
  }
  .card-back {
    top: 530px;
    height: 418px;
    background: var(--white);
    color: var(--text-dark);
  }
  .front-mark {
    position: absolute;
    left: 334px;
    top: 168px;
    width: 70px;
    height: 70px;
    background: var(--white);
  }
  .front-name {
    position: absolute;
    left: 0; right: 0;
    top: 250px;
    text-align: center;
    font-size: 43px;
    font-weight: 400;
    letter-spacing: 0.5px;
    line-height: 1;
  }
  .front-role {
    position: absolute;
    left: 153px;
    width: 432px;
    top: 299px;
    display: flex;
    align-items: center;
    gap: 12px;
    font-size: 17px;
    letter-spacing: 4.2px;
    line-height: 1;
  }
  .front-role .rule { flex: 1; height: 1.5px; background: var(--white); }
  .back-brand {
    position: absolute;
    left: 41px;
    top: 80px;
    display: flex;
    align-items: center;
    gap: 12px;
    font-size: 28px;
    font-weight: 500;
    line-height: 1;
    color: var(--brand-blue);
  }
  .back-brand .brand-square {
    width: 26px; height: 26px; background: var(--brand-blue);
  }
  .back-name {
    position: absolute; left: 41px; top: 165px;
    font-size: 27px; font-weight: 700; color: var(--brand-blue);
  }
  .back-role { position: absolute; left: 41px; top: 199px; font-size: 20px; }
  .back-address { position: absolute; left: 41px; top: 243px; font-size: 20px; line-height: 27px; }
  .contact-list {
    position: absolute; left: 41px; top: 312px;
    margin: 0; padding: 0; list-style: none;
    font-size: 20px; line-height: 26.5px;
  }
  .contact-list li { display: flex; align-items: center; gap: 8px; }
  .contact-list svg { width: 14px; height: 14px; fill: var(--brand-blue); flex: none; }
  .web-accent { color: var(--brand-blue); }
  .trainer-photo {
    position: absolute;
    left: 465px; top: 20px;
    width: 253px; height: 398px;
    background: linear-gradient(180deg, var(--photo-light) 0%, #8a8a8a 30%, var(--photo-dark) 100%);
    border-radius: 110px 110px 0 0;
  }
</style>
</head>
<body>
<div class="canvas">
  <section class="card card-front">
    <div class="front-mark"></div>
    <div class="front-name">TOBIAS KELLINGER</div>
    <div class="front-role"><span class="rule"></span><span>PERSONAL TRAINER</span><span class="rule"></span></div>
  </section>

  <section class="card card-back">
    <div class="back-brand"><span class="brand-square"></span><span>Kellinger Coaching</span></div>
    <div class="back-name">Tobias Kellinger</div>
    <div class="back-role">Personal Trainer</div>
    <div class="back-address">Lindenfeldweg 14<br>80412 München</div>
    <ul class="contact-list">
      <li><svg viewBox="0 0 24 24"><path d="M6.6 10.8a15.1 15.1 0 0 0 6.6 6.6l2.2-2.2a1 1 0 0 1 1-.25 11.4 11.4 0 0 0 3.6.57 1 1 0 0 1 1 1V20a1 1 0 0 1-1 1A17 17 0 0 1 3 4a1 1 0 0 1 1-1h3.5a1 1 0 0 1 1 1c0 1.25.2 2.45.57 3.57a1 1 0 0 1-.25 1z"/></svg><span>0163/2918374</span></li>
      <li><svg viewBox="0 0 24 24"><path d="M2 5h20v14H2z M2 5l10 8 10-8"/></svg><span>t.kellinger@postwerk.de</span></li>
      <li><svg viewBox="0 0 24 24"><circle cx="12" cy="12" r="10"/></svg><span>www.<span class="web-accent">tobiaskellinger</span>.de</span></li>
    </ul>
    <div class="trainer-photo" role="img" aria-label="Schwarzweiß-Porträt des Trainers mit verschränkten Armen im dunklen Sportshirt"></div>
  </section>
</div>
</body>
</html>
```